Fundraiser Flyer and Email Template

We are looking for a flexible coordinated flyer and email template. The feel of both should be more formal or professional. We are not looking for an overly "political" design that features American flags or other "political" symbols.

We are a political fundraising firm that works with elected officials to set up fundraisers for their campaigns. We send the invites to these events via US Mail and email, so we are looking for a standardized template that will work as both an 8.5 x 11 inch printed flyer, as well as an email template.

The information in the email will be text, but images can be used for formatting.

Some clients have a campaign logo, others do not. The format should be flexible enough to either include the logo, or leave it out. Size also varies.

Any colors in the template should be editable so we can match logos as we get them.

We're open to any format that allows us to edit the format as needed. This would include Photoshop, Microsoft Word, etc.

The text of the invite should include space for:

---------------------------------------
NAME
DISTRICT NUMBER AND OFFICE

DATE OF EVENT
TIME OF EVENT

LOCATION
LOCATION ADDRESS
LOCATION CITY, STATE, ZIP

SUGGESTED CONTRIBUTION LEVELS (Typically 3 levels are provided such as Gold: $1,000, Silver: $500, Bronze: $250)

ADDRESS TO SEND CHECKS TO

RSVP CONTACT INFORMATION

The invite will also need fine-print at the bottom that reads:
"Pennsylvania law allows personal, partnership, and PAC contributions. By law we cannot accept corporate contributions
Paid for by [NAME]"

It Professional

Serif
Sans Serif

• Must have spaces for:
• NAME
• DISTRICT NUMBER AND OFFICE
• DATE OF EVENT
• TIME OF EVENT
• LOCATION
• LOCATION ADDRESS
• LOCATION CITY, STATE, ZIP
• SUGGESTED CONTRIBUTION LEVELS (Typically 3 levels are provided such as Gold: $1,000, Silver: $500, Bronze: $250)
• ADDRESS TO SEND CHECKS TO
• RSVP CONTACT INFORMATION
• The invite will also need fine-print at the bottom that reads:
• "Pennsylvania law allows personal, partnership, and PAC contributions. By law we cannot accept corporate contributions
• Paid for by [NAME]"
• It should not be overly "political".

```html
<!DOCTYPE html>
<html lang="en">
<head>
<meta charset="utf-8">
<title>Fundraising Reception Invitation</title>
<link href="https://fonts.googleapis.com/css2?family=Archivo+Black&family=Marcellus+SC&family=Roboto+Condensed:wght@400;700&display=swap" rel="stylesheet">
<style>
  :root{
    --green:#0b7a5a;
    --green-dark:#06654a;
    --gold:#f2c500;
    --gold-line:#e6c21c;
    --cream-top:#ffffff;
    --cream-bottom:#fbeebb;
    --page:#cdb894;
    --ink:#0b7052;
  }
  html,body{margin:0;padding:0;overflow:hidden}
  body{width:1200px;height:898px;background:var(--page);position:relative}
  .flyer{
    position:absolute;left:270px;top:20px;width:660px;height:858px;
    background:linear-gradient(180deg,var(--cream-top) 25%,var(--cream-bottom) 88%);
    box-shadow:0 10px 30px rgba(60,40,10,.35);overflow:hidden;
    color:var(--ink);text-align:center;
  }
  .header-band{position:absolute;left:0;top:0;width:660px;height:190px}
  .header-text{
    position:absolute;left:0;top:44px;width:660px;
    font-family:"Marcellus SC",serif;color:#fff;font-size:27px;line-height:36px;letter-spacing:1px;
  }
  .header-text .star{color:var(--gold);font-size:20px}
  .campaign-name{
    position:absolute;left:0;top:196px;width:660px;line-height:44px;
    font-family:"Archivo Black",sans-serif;font-size:34px;color:var(--green);
  }
  .candidate-name{
    position:absolute;left:0;top:246px;width:660px;line-height:46px;
    font-family:"Archivo Black",sans-serif;font-size:36px;color:var(--green-dark);
  }
  .candidate-office{
    position:absolute;left:0;top:296px;width:660px;line-height:32px;
    font-family:"Archivo Black",sans-serif;font-size:24px;color:var(--green-dark);
  }
  .candidate-office sup{font-size:13px;line-height:0}
  .date-ribbon{position:absolute;left:20px;top:466px;width:620px;height:90px}
  .portrait-frame{position:absolute;left:257px;top:338px;width:140px;height:140px;background:#fff;border-right:6px solid var(--gold-line);border-bottom:6px solid var(--gold-line);box-shadow:2px 3px 6px rgba(0,0,0,.2)}
  .portrait{position:absolute;left:8px;top:8px;width:124px;height:124px;background:linear-gradient(180deg,#9a9a9a,#6f6f6f)}
  .date-text{
    position:absolute;left:0;top:487px;width:660px;line-height:40px;
    font-family:"Roboto Condensed",sans-serif;font-weight:700;font-size:30px;color:var(--gold);
  }
  .venue{
    position:absolute;left:0;top:552px;width:660px;
    font-family:"Roboto Condensed",sans-serif;font-weight:700;font-size:26px;line-height:33px;color:var(--green-dark);
  }
  .levels-title{
    position:absolute;left:0;top:630px;width:660px;line-height:26px;
    font-family:"Roboto Condensed",sans-serif;font-size:21px;letter-spacing:1px;text-decoration:underline;color:var(--green);
  }
  .levels{
    position:absolute;left:0;top:658px;width:660px;line-height:24px;
    font-family:"Roboto Condensed",sans-serif;font-size:18px;color:var(--green);
  }
  .levels .dot{display:inline-block;width:8px;height:8px;border-radius:50%;margin:0 5px 2px 12px}
  .dot.gold{background:#e2c44a}.dot.silver{background:#cfd4d6}.dot.bronze{background:#e2a384}
  .checks{
    position:absolute;left:0;top:686px;width:660px;
    font-family:"Roboto Condensed",sans-serif;font-weight:700;font-size:18px;line-height:24px;color:var(--green-dark);
  }
  .footer-curve{position:absolute;left:0;top:740px;width:660px;height:118px}
  .footer{
    position:absolute;left:0;top:786px;width:660px;
    font-family:"Roboto Condensed",sans-serif;color:var(--green);
  }
  .rsvp{font-weight:700;font-size:15px;line-height:18px;display:flex;justify-content:center;gap:18px;align-items:center}
  .rsvp svg{vertical-align:middle;margin-right:4px}
  .fine-print{font-size:12px;line-height:15px;margin-top:3px}
</style>
</head>
<body>
<div class="flyer">
  <svg class="header-band" viewBox="0 0 660 190" aria-hidden="true">
    <defs><linearGradient id="bandFill" x1="0" y1="0" x2="0" y2="1"><stop offset="0" stop-color="#0d8763"/><stop offset="1" stop-color="#06654a"/></linearGradient></defs>
    <path d="M0 0H660V120Q330 205 0 150Z" fill="url(#bandFill)"/>
    <path d="M0 150Q330 205 660 120" fill="none" stroke="var(--gold-line)" stroke-width="4"/>
  </svg>
  <div class="header-text"><span class="star">★</span> Please Join Us for a <span class="star">★</span><br>Special Fundrasising Reception</div>

  <div class="campaign-name">Whitford Campaign</div>
  <div class="candidate-name">Daniel Whitford</div>
  <div class="candidate-office">State Senator, 46<sup>th</sup> Senate Sistrict</div>

  <svg class="date-ribbon" viewBox="0 0 620 90" aria-hidden="true">
    <polygon points="0,20 40,20 25,45 40,70 0,70 18,45" fill="var(--green-dark)"/>
    <polygon points="620,20 580,20 595,45 580,70 620,70 602,45" fill="var(--green-dark)"/>
    <rect x="30" y="12" width="560" height="58" fill="var(--green)"/>
  </svg>
  <div class="portrait-frame"><div class="portrait" role="img" aria-label="Candidate portrait photo"></div></div>
  <div class="date-text">Tuesday, June 17th | 5:00pm - 7:00pm</div>

  <div class="venue">Harlow Arts Center 52 Market Street,<br>Rivermont, FL 33100</div>
  <div class="levels-title">CONTRIBUTION LEVELS</div>
  <div class="levels"><span class="dot gold"></span>Gold: $1,000 <span class="dot silver"></span>Silver: $500 <span class="dot bronze"></span>Bronze: $250</div>
  <div class="checks">Make checks payable to : XXXXXXXXXXXX<br>P.O. Box 1275, Lakeview, FL 33400-1275</div>

  <svg class="footer-curve" viewBox="0 0 660 118" aria-hidden="true">
    <path d="M0 50Q330 -10 660 30V118H0Z" fill="#fff"/>
    <path d="M0 50Q330 -10 660 30" fill="none" stroke="var(--green)" stroke-width="3"/>
    <polygon points="302,22 305,30 313,30 307,35 309,43 302,38 295,43 297,35 291,30 299,30" fill="var(--green)"/>
    <polygon points="330,16 334,26 344,26 336,32 339,42 330,36 321,42 324,32 316,26 326,26" fill="var(--gold)"/>
    <polygon points="358,22 361,30 369,30 363,35 365,43 358,38 351,43 353,35 347,30 355,30" fill="var(--green)"/>
  </svg>
  <div class="footer">
    <div class="rsvp">
      <span>RSVP CONTACT</span>
      <span><svg width="12" height="14" viewBox="0 0 12 14"><path d="M2 1l3 3-1.5 2a8 8 0 0 0 3 4l2-1.5 3 3-2 2C5 13 0 7 0 3z" fill="var(--green)"/></svg>555-010-2468</span>
      <span><svg width="16" height="11" viewBox="0 0 16 11"><rect width="16" height="11" fill="var(--green)"/><path d="M0 0l8 6 8-6" stroke="#fff" fill="none"/></svg>rsvp@whitfordevents.org</span>
    </div>
    <div class="fine-print">Pennsylvania law allows personal, partnership, and PAC contributions.<br>By law we cannot accept corporate contributions<br>Paid for by [NAME]</div>
  </div>
</div>
</body>
</html>
```